Mobile Friendly Lead Generation Landing Page

We are a web marketing company that specialized in web lead generation. Recently we have started buying media from mobile devices and we need a mobile interface(landing page) where we can collect user data in an effective manner.

Our current mobile landing page is:
http://www.pathwaylocate.example.com/lp13d/index.aspx?a=true&source=591483
Through this you can see what the steps/questions users need to answer to get matched to a school. We need the design for the whole process.

We are pretty open for design ideas and our goal is to make this mobile optimized landing page have the look and feel of an app...but not an app.
There are several questions in the process but we are open to changing the way they are presented. As in, you can have one question at a time or a few.
The goal is to make this EXTREMELY EASY for users to interact with.

One example that we have liked is:
http://tutorhubnet.example.com/schools/72615-page1.thub (please note that this opens only on mobile devices)

Some of these screenshots are attached.

Our web form looks like this:
http://www.pathwaylocate.example.com/lp88/index.aspx?a=true

```html
<!DOCTYPE html>
<html lang="en">
<head>
<meta charset="utf-8">
<title>PathwayLocate – Field of Interest</title>
<link rel="stylesheet" href="https://fonts.googleapis.com/css2?family=Oswald:wght@500;600&family=PT+Sans:wght@400;700&family=Arimo:wght@400&display=swap">
<style>
  :root {
    --header-dark: #1b2e33;
    --header-strip: #172a2f;
    --page-green: #8fb33d;
    --panel-green: #b0d066;
    --olive: #5d7c0c;
    --olive-deep: #5a7a0b;
    --option-bg: #effcd0;
    --cream: #f2f7dc;
    --note-text: #3f5914;
    --footer-band: #5f7f0b;
    --white: #ffffff;
  }
  * { box-sizing: border-box; margin: 0; padding: 0; }
  html, body { width: 1200px; height: 2238px; overflow: hidden; }
  body { background: var(--page-green); position: relative; font-family: "PT Sans", sans-serif; }

  .site-header { position: absolute; left: 0; top: 0; width: 1200px; height: 206px; background: var(--header-dark); }
  .site-header .strip { position: absolute; left: 280px; top: 0; width: 920px; height: 24px; background: var(--header-strip); }
  .brand { position: absolute; left: 0; top: 0; width: 1200px; height: 206px; display: flex; align-items: center; justify-content: center; gap: 24px; }
  .brand-dot { width: 44px; height: 44px; border-radius: 50%; background: var(--panel-green); }
  .brand-name { font-family: "Oswald", sans-serif; font-weight: 600; font-size: 76px; color: var(--white); letter-spacing: 1px; }

  .hero-title { position: absolute; top: 222px; width: 1200px; text-align: center; font-family: "Oswald", sans-serif; font-weight: 600; font-size: 50px; color: var(--white); }
  .hero-sub { position: absolute; top: 290px; width: 1200px; text-align: center; font-weight: 700; font-size: 32px; color: var(--cream); }

  .form-panel { position: absolute; left: 36px; top: 350px; width: 1130px; height: 1510px; background: var(--panel-green); }
  .form-title { position: absolute; top: 22px; width: 100%; text-align: center; font-family: "Oswald", sans-serif; font-weight: 600; font-size: 80px; color: var(--olive); letter-spacing: -1px; }
  .progress { position: absolute; left: 136px; top: 132px; width: 874px; height: 20px; border-radius: 10px; background: var(--olive-deep); }
  .progress-label { position: absolute; top: 160px; width: 100%; text-align: center; font-family: "Arimo", sans-serif; font-size: 24px; color: #4b5d28; }

  .question { position: absolute; left: 50px; top: 238px; width: 1036px; height: 88px; border-radius: 20px; background: var(--header-dark); color: var(--cream); font-weight: 700; font-size: 44px; display: flex; align-items: center; justify-content: center; }

  .options { position: absolute; left: 50px; top: 368px; width: 1036px; display: grid; grid-template-columns: 504px 504px; column-gap: 28px; row-gap: 30px; list-style: none; }
  .option { height: 90px; border-radius: 8px; background: var(--option-bg); color: var(--olive); font-family: "Oswald", sans-serif; font-weight: 600; font-size: 38px; display: flex; align-items: center; justify-content: center; letter-spacing: -0.5px; }

  .back { position: absolute; left: 46px; top: 1354px; display: flex; align-items: center; gap: 24px; }
  .back-label { font-family: "Oswald", sans-serif; font-weight: 600; font-size: 112px; line-height: 1; color: var(--olive); }

  .notes { position: absolute; top: 1884px; left: 60px; width: 1080px; text-align: center; font-family: "Arimo", sans-serif; font-size: 24px; line-height: 28px; color: var(--note-text); }
  .notes p + p { margin-top: 44px; }

  .site-footer { position: absolute; left: 0; top: 2094px; width: 1200px; height: 144px; background: var(--footer-band); color: var(--white); font-family: "Arimo", sans-serif; font-size: 24px; text-align: center; padding-top: 38px; line-height: 44px; }
</style>
</head>
<body>
  <header class="site-header">
    <div class="strip"></div>
    <div class="brand">
      <span class="brand-dot"></span>
      <span class="brand-name">PathwayLocate</span>
    </div>
  </header>

  <h1 class="hero-title">GET MATCHED TO ONLINE &amp; LOCAL COLLEGES NOW</h1>
  <p class="hero-sub">Find Online &amp; Campus Colleges</p>

  <main class="form-panel">
    <h2 class="form-title">FILL OUT OUR 2 MINUTE FORM</h2>
    <div class="progress"></div>
    <p class="progress-label">Amount Completed</p>

    <div class="question">Please select your field of interest:</div>

    <ul class="options">
      <li class="option">ART &amp; DESIGN</li>
      <li class="option">BUSINESS</li>
      <li class="option">CRIMINAL JUSTICE</li>
      <li class="option">EDUCATION &amp; TEACHING</li>
      <li class="option">ENGINEERING</li>
      <li class="option">HEALTH CULTURE</li>
      <li class="option">HUMAN SERVICES</li>
      <li class="option">LEGAL &amp; PARELEGAL</li>
      <li class="option">LIBERAL ARTS</li>
      <li class="option">NURSING</li>
      <li class="option">POLITICAL SCIENCE</li>
      <li class="option">PSYCHOLOGY</li>
      <li class="option">RELIGIOUS STUDIES</li>
      <li class="option">SCIENCE &amp; MATH</li>
      <li class="option">SOCIAL SERVICES</li>
      <li class="option">TECHNOLOGY</li>
    </ul>

    <div class="back">
      <svg width="92" height="92" viewBox="0 0 92 92" aria-hidden="true">
        <circle cx="46" cy="46" r="46" fill="var(--olive)"/>
        <polygon points="28,46 58,28 58,64" fill="var(--panel-green)"/>
      </svg>
      <span class="back-label">BACK</span>
    </div>
  </main>

  <section class="notes">
    <p>Financial Aid is available for those who qualify. To see if you qualify for financial aid of any kind you must speak with a representative of one of our partnering schools.</p>
    <p>Program outcomes vary according to each institution's specific curriculum, and employment opportunities are not guaranteed.</p>
  </section>

  <footer class="site-footer">
    <div>Copyright @ PathwayLocate.example.com. All Rights Reserved.</div>
    <div>Privacy Policy | Unsubscribe | Advertising with us</div>
  </footer>
</body>
</html>
```